Business Goals Posters for display within company office and factory.

We have three (3) high level business goals we want to display in the office and factory areas of the business.

1. Under the heading of "QUALITY"
"We will have pride and ownership of every product and service delivered to our customers."

2. Under the heading of "PRODUCTIVITY"
"We will put the customer's expectations first and ensure our team is empowered to do so."

3. Under the heading of "SAFETY"
"We will shift our culture to ensure safety is our first thought on every job."

We would like a matching set of posters with these three headings and statements with a background suitable for display in a business environment. The posters will be displayed in sizes from A4 and A2.
The company's logo is Red and Black (see attachment) .
We make Electric and Hydraulic power packs for industrial market.
our website will give you an idea of what we do www.tarnwickdrives.com.au

Industry/Entity Type

Power Generation

Colors

Designer to choose colors to be used in the design.

Requirements
Must have
• The posters must use the exact text provided and have the headings listed.
• the three posters must have a common theme. they can be different in back ground but when side by side must look like a set.
• Be suitable for display as A4 and as A2.
Nice to have
• The text needs the be the star, the background needs to draw attention to the poster and the text with out over powering it,
Should not have
• not have photo's of generators or equipment as backgrounds

```html
<!DOCTYPE html>
<html lang="en">
<head>
<meta charset="utf-8">
<title>Business Goals Posters</title>
<link rel="stylesheet" href="https://fonts.googleapis.com/css2?family=Anton&family=Open+Sans:wght@400&display=swap">
<style>
  :root {
    --backdrop: #d6d8da;
    --red-deep: #c3151a;
    --red-bright: #ec1c24;
    --grey: #646464;
    --white: #ffffff;
    --ink: #1e1e1e;
    --rule-dark: #6f6f6f;
    --rule-light: #c9c9c9;
  }
  * { box-sizing: border-box; margin: 0; padding: 0; }
  html, body { width: 1200px; height: 1200px; overflow: hidden; }
  body {
    background: var(--backdrop);
    position: relative;
    font-family: "Anton", "Impact", sans-serif;
  }
  .poster {
    position: absolute;
    top: 317px;
    width: 387px;
    height: 546px;
    display: flex;
    flex-direction: column;
  }
  .poster--quality { left: 10px; }
  .poster--productivity { left: 406px; }
  .poster--safety { left: 803px; }

  .poster__header {
    height: 133px;
    display: flex;
    align-items: center;
    justify-content: center;
  }
  .poster__heading {
    font-family: "Anton", "Impact", sans-serif;
    font-weight: 400;
    font-size: 70px;
    line-height: 1;
    letter-spacing: 0.5px;
  }
  .poster__body {
    flex: 1;
    position: relative;
    padding: 0 38px;
  }
  .poster__statement {
    position: absolute;
    top: 44px;
    left: 20px;
    right: 20px;
    text-align: center;
    font-size: 20px;
    line-height: 25px;
  }
  .poster__brand {
    position: absolute;
    top: 188px;
    left: 0;
    right: 0;
    display: flex;
    align-items: center;
    justify-content: center;
    gap: 10px;
  }
  .brand__mark { width: 22px; height: 22px; }
  .brand__name { font-size: 30px; line-height: 1; letter-spacing: 0.5px; }
  .poster__rule {
    position: absolute;
    top: 292px;
    left: 39px;
    right: 39px;
    height: 1px;
  }
  .poster__prompt {
    position: absolute;
    top: 302px;
    left: 42px;
    font-family: "Open Sans", Arial, sans-serif;
    font-size: 17px;
  }
  .poster__answer {
    position: absolute;
    top: 342px;
    right: 39px;
    height: 33px;
    padding: 0 8px;
    display: flex;
    align-items: center;
    border-radius: 3px;
    font-size: 21px;
    line-height: 1;
  }

  /* Quality */
  .poster--quality .poster__header { background: var(--red-deep); }
  .poster--quality .poster__heading { color: var(--white); }
  .poster--quality .poster__body { background: var(--white); }
  .poster--quality .poster__statement { color: var(--red-deep); }
  .poster--quality .brand__name { color: var(--ink); }
  .poster--quality .brand__mark { fill: var(--red-bright); }
  .poster--quality .poster__rule { background: var(--rule-dark); }
  .poster--quality .poster__prompt { color: #444; }
  .poster--quality .poster__answer { background: var(--red-deep); color: var(--white); }

  /* Productivity */
  .poster--productivity .poster__header { background: var(--red-bright); }
  .poster--productivity .poster__heading { color: var(--ink); }
  .poster--productivity .poster__body { background: var(--grey); }
  .poster--productivity .poster__statement { color: #ececec; }
  .poster--productivity .brand__name { color: var(--ink); }
  .poster--productivity .brand__mark { fill: var(--red-deep); }
  .poster--productivity .poster__rule { background: var(--rule-light); opacity: 0.5; }
  .poster--productivity .poster__prompt { color: #e6e6e6; }
  .poster--productivity .poster__answer { background: #f0f0f0; color: var(--ink); }

  /* Safety */
  .poster--safety .poster__header { background: var(--white); }
  .poster--safety .poster__heading { color: var(--red-deep); }
  .poster--safety .poster__body { background: var(--red-bright); }
  .poster--safety .poster__statement { color: var(--white); }
  .poster--safety .brand__name { color: var(--ink); }
  .poster--safety .brand__mark { fill: #f47a6a; }
  .poster--safety .poster__rule { background: var(--rule-light); opacity: 0.6; }
  .poster--safety .poster__prompt { color: #f6f6f6; }
  .poster--safety .poster__answer { background: var(--white); color: var(--red-deep); }
</style>
</head>
<body>

  <section class="poster poster--quality">
    <header class="poster__header"><h2 class="poster__heading">QUALITY</h2></header>
    <div class="poster__body">
      <p class="poster__statement">"We will have pride and ownership<br>of every product and service<br>delivered to our customers."</p>
      <div class="poster__brand">
        <svg class="brand__mark" viewBox="0 0 22 22" aria-hidden="true"><rect width="22" height="22"/></svg>
        <span class="brand__name">Tarnwick Drives</span>
      </div>
      <div class="poster__rule"></div>
      <p class="poster__prompt">What do you think?</p>
      <span class="poster__answer">Definitely</span>
    </div>
  </section>

  <section class="poster poster--productivity">
    <header class="poster__header"><h2 class="poster__heading">PRODUCTIVITY</h2></header>
    <div class="poster__body">
      <p class="poster__statement">"We will put the customer's<br>expectations first and ensure our<br>team is empowered to do so."</p>
      <div class="poster__brand">
        <svg class="brand__mark" viewBox="0 0 22 22" aria-hidden="true"><rect width="22" height="22"/></svg>
        <span class="brand__name">Tarnwick Drives</span>
      </div>
      <div class="poster__rule"></div>
      <p class="poster__prompt">What do you think?</p>
      <span class="poster__answer">Absolutely</span>
    </div>
  </section>

  <section class="poster poster--safety">
    <header class="poster__header"><h2 class="poster__heading">SAFETY</h2></header>
    <div class="poster__body">
      <p class="poster__statement">"We will shift our culture<br>to ensure safety is<br>our first thought on every job."</p>
      <div class="poster__brand">
        <svg class="brand__mark" viewBox="0 0 22 22" aria-hidden="true"><rect width="22" height="22"/></svg>
        <span class="brand__name">Tarnwick Drives</span>
      </div>
      <div class="poster__rule"></div>
      <p class="poster__prompt">What do you think?</p>
      <span class="poster__answer">Undeniably</span>
    </div>
  </section>

</body>
</html>
```